Homes, Invest in Non-performing loans

We need only 3 web pages, one for the home, one for the content, one for the properties.
The main focus of our business is to offer non performing loans (before foreclosures) to the general public. All the non-performing mortgages will end in a house, an apartment, a store, etc.
Our customers are able to invest from 10,000usd to 1,000,000usd (average 50,000usd).
Our customers' usual focus groups are employees who want second earnings, perceiving the business feeling without outlay time. They look for a solid finance sense corporation that confers them certainty.
Nearly all our clients desire the house, apartment, store, etc. more than the actual earnings.
The name of our company is BRAMLEY
Reason: We value the time and effort you already invest in our project. We realize that we did't come back on some of the doubts requested by the designers. It will be inequitable to the designers who prerequisite our feedback. We also appreciate the comprehension of the community in this postponement.
Reason: Designers,
We really apreciate all the time and effort you put on our project. From the begining we ask for 3 pages, so now we will leave the 10 finalist and provide some extra time to submit the other 2 pages.
We will race the price in 10%
Target Market(s)
Our customers average investors works as employees and want to have a second income or business without spending time. (People from 35 to 50)
Industry/Entity Type
Finance
Requirements
Should not have
- FLASH

```html
<!DOCTYPE html>
<html lang="en">
<head>
<meta charset="utf-8">
<title>Bramley — Invest in Non-performing Loans</title>
<link href="https://fonts.googleapis.com/css2?family=PT+Sans:ital,wght@0,400;0,700;1,700&family=Open+Sans:wght@400;600&display=swap" rel="stylesheet">
<style>
:root{
  --olive:#878a22;
  --olive-light:#c5c84a;
  --orange:#f7941d;
  --ink:#333;
  --text:#555;
  --muted:#888;
  --panel:#f0f0f0;
  --panel-dark:#e4e4e4;
  --footer:#383838;
  --footer-bar:#262626;
  --footer-text:#aaa;
}
*{box-sizing:border-box;margin:0;padding:0}
html,body{width:990px;height:1200px;overflow:hidden;background:#fff}
body{font-family:"Open Sans",sans-serif;color:var(--text)}
.page{position:relative;width:1200px;height:1454px;transform:scale(.825);transform-origin:0 0}
.abs{position:absolute}
.head{font-family:"PT Sans",sans-serif;font-weight:700;text-transform:uppercase}

/* header */
.brand{left:110px;top:40px;display:flex;align-items:center;gap:8px}
.brand-mark{width:22px;height:22px;background:var(--olive)}
.brand-name{font-family:"PT Sans",sans-serif;font-weight:700;font-size:30px;color:var(--ink);letter-spacing:1px}
.account{left:717px;top:26px;font-size:11px;color:var(--ink);font-family:"PT Sans",sans-serif}
.account span{margin:0 7px;color:#999}
.search{left:876px;top:18px;width:214px;height:28px;border:1px solid #ccc;display:flex}
.search .field{flex:1;padding:4px 10px;font-style:italic;font-size:13px;color:#999;font-weight:600}
.search .btn{width:32px;background:#bdbdbd;display:flex;align-items:center;justify-content:center}
.nav{top:84px;font-family:"PT Sans",sans-serif;font-size:14px;color:var(--ink);text-transform:uppercase}
.nav.active{color:var(--olive)}

/* hero */
.offer-head{left:110px;top:120px;width:352px;height:70px;background:var(--olive);padding:14px 10px}
.offer-head h2{font-size:19px;color:#fff;line-height:22px}
.offer-head p{font-family:"PT Sans",sans-serif;font-size:15px;color:var(--olive-light)}
.photo-advisor{left:110px;top:190px;width:352px;height:267px;background:linear-gradient(90deg,#d6d6d6,#8a8a8a 60%,#c6c6c6)}
.photo-house{left:462px;top:120px;width:352px;height:267px;background:linear-gradient(180deg,#e8e8e8,#b5b5b5 70%,#7d7d7d)}
.invest-band{left:462px;top:387px;width:352px;height:70px;background:#3c3c3c;padding:10px 16px}
.invest-band h2{font-size:22px;color:var(--olive-light);line-height:26px}
.invest-band p{font-family:"PT Sans",sans-serif;font-size:15px;color:#fff}
.contact-head{left:814px;top:120px;width:276px;height:70px;background:var(--orange);padding:16px 14px}
.contact-head h2{font-size:18px;color:#fff;line-height:20px}
.contact-head p{font-family:"PT Sans",sans-serif;font-size:15px;color:#fff}
.contact-form{left:814px;top:190px;width:276px;height:267px;background:var(--panel)}
.input{position:absolute;left:14px;width:252px;height:29px;background:#fff;border:1px solid #ccc;padding:6px 8px;font-size:12px;font-style:italic;font-weight:600;color:#999}
.submit{position:absolute;left:77px;top:218px;width:121px;height:32px;background:var(--olive);display:flex}
.submit .ico{width:36px;background:#6d6f18;display:flex;align-items:center;justify-content:center}
.submit .lbl{flex:1;text-align:center;line-height:32px;color:#fff;font-family:"PT Sans",sans-serif;font-size:15px}

/* about */
.section-title{font-family:"PT Sans",sans-serif;font-weight:700;font-size:18px;color:var(--olive);text-transform:uppercase}
.about-text{left:109px;top:527px;width:320px;font-size:12px;line-height:17px}
.about-text p{margin-bottom:17px}
.btn-more{height:31px;background:var(--orange);color:#fff;font-size:12px;line-height:31px;padding-left:10px}
.btn-more b{font-weight:400;margin-right:7px}

/* news */
.news{left:462px;top:499px;width:628px;height:237px;background:var(--panel)}
.news-date{position:absolute;left:13px;font-family:"PT Sans",sans-serif;font-weight:700;font-size:14px;color:#999}
.news-title{position:absolute;font-family:"PT Sans",sans-serif;font-weight:700;font-style:italic;font-size:16px;color:var(--olive);white-space:nowrap}
.news-row{position:absolute;left:0;width:628px;height:35px;background:var(--panel-dark);border-top:1px solid #d8d8d8}
.news-row .date{top:9px}
.news-row .news-title{top:7px}
.news-row .go{position:absolute;right:0;top:0;width:36px;height:35px;background:var(--orange);display:flex;align-items:center;justify-content:center}
.news-sep{position:absolute;left:103px;width:1px;background:#ccc}
.news-photo{position:absolute;left:118px;top:42px;width:159px;height:103px;background:linear-gradient(90deg,#7f9bb8,#c9b3a0 55%,#6f6f6f)}
.news-body{position:absolute;left:294px;top:42px;width:324px;font-size:12px;line-height:17px}
.news-more{position:absolute;right:13px;top:131px;font-size:12px;color:var(--orange)}

/* worldwide */
.rule{left:109px;width:981px;height:1px;background:#ddd}
.map{left:109px;top:810px;width:245px;height:130px;background:radial-gradient(ellipse at 50% 45%,#e2e2e2,#f3f3f3 70%,#fff)}
.world-text{left:376px;top:820px;width:410px;font-size:13px;line-height:20px}
.feature{left:815px;width:274px;height:41px;border-radius:21px;background:var(--panel);font-size:14px;color:var(--text)}
.feature .dot{position:absolute;left:0;top:0;width:41px;height:41px;border-radius:50%;background:var(--orange);display:flex;align-items:center;justify-content:center}
.feature span{position:absolute;left:57px;top:11px}

/* clients */
.clients{left:109px;top:1024px;width:981px;height:85px;background:#f2f2f2;display:flex;align-items:center;justify-content:space-around}
.client{display:flex;align-items:center;gap:8px;font-family:"Open Sans",sans-serif;font-weight:600;font-size:24px;color:#3a3a3a}
.client i{display:block;width:20px;height:20px;background:#9a9a9a}

/* footer */
.footer{left:0;top:1170px;width:1200px;height:244px;background:var(--footer)}
.footer h3{position:absolute;top:42px;font-family:"PT Sans",sans-serif;font-weight:400;font-size:13px;color:var(--olive-light);text-transform:uppercase;letter-spacing:.5px}
.quick{position:absolute;left:109px;top:72px;font-size:12px;line-height:23px;color:var(--footer-text);text-transform:uppercase;letter-spacing:.8px;list-style:none}
.tweet{position:absolute;left:307px;width:412px;height:56px}
.tweet .avatar{position:absolute;left:0;top:0;width:46px;height:46px;background:linear-gradient(#9a9a9a,#5a5a5a)}
.tweet .name{position:absolute;left:60px;top:0;font-size:13px;line-height:18px;color:#eee;letter-spacing:.5px}
.tweet .msg{position:absolute;left:60px;top:18px;width:352px;font-family:"PT Sans",sans-serif;font-size:11px;line-height:20px;color:var(--footer-text);white-space:nowrap}
.tweet-rule{position:absolute;left:307px;top:138px;width:412px;height:1px;background:#666}
.address{position:absolute;left:799px;top:70px;font-size:12px;line-height:18px;color:var(--footer-text)}
.phone{position:absolute;left:799px;top:128px;font-size:14px;color:var(--footer-text);display:flex;align-items:center;gap:10px}
.mail{position:absolute;left:799px;top:148px;font-size:12px;color:var(--footer-text);display:flex;align-items:center;gap:10px}
.social{position:absolute;top:177px;width:22px;height:22px;background:#6a6a6a}
.bottom-bar{left:0;top:1414px;width:1200px;height:40px;background:var(--footer-bar);font-size:12px;color:#bbb}
.bottom-bar .copy{position:absolute;left:110px;top:12px}
.bottom-bar .links{position:absolute;right:124px;top:12px;display:flex;gap:33px}
</style>
</head>
<body>
<div class="page">

  <header>
    <div class="abs brand"><i class="brand-mark"></i><span class="brand-name">BRAMLEY</span></div>
    <div class="abs account">LOGIN<span>|</span>REGISTER NOW</div>
    <div class="abs search"><div class="field">Search...</div><div class="btn"><svg width="14" height="14" viewBox="0 0 14 14"><circle cx="5.5" cy="5.5" r="4" fill="none" stroke="#fff" stroke-width="1.6"/><path d="M8.5 8.5l4 4" stroke="#fff" stroke-width="1.8"/></svg></div></div>
    <nav>
      <div class="abs nav active" style="left:550px">Home</div>
      <div class="abs nav" style="left:628px">About Us</div>
      <div class="abs nav" style="left:732px">Auction</div>
      <div class="abs nav" style="left:829px">Access</div>
      <div class="abs nav" style="left:905px">Initiation</div>
      <div class="abs nav" style="left:1011px">Contact Us</div>
    </nav>
  </header>

  <section class="hero">
    <div class="abs offer-head"><h2 class="head">We offer non performing loans</h2><p>Buy property save up to 60% of its market value.</p></div>
    <div class="abs photo-advisor" role="img" aria-label="Black and white portrait of a smiling advisor with arms crossed"></div>
    <div class="abs photo-house" role="img" aria-label="Black and white photo of a two-storey house with a front porch"></div>
    <div class="abs invest-band"><h2 class="head">We play &amp; invest safe</h2><p>Lorem ipsum dolor sit amet, consectetuer.</p></div>
    <div class="abs contact-head"><h2 class="head">Contact us now!</h2><p>To stay updated with latest updates.</p></div>
    <div class="abs contact-form">
      <div class="input" style="top:19px">Your Name</div>
      <div class="input" style="top:58px">Your Email Address</div>
      <div class="input" style="top:97px">Your Phone Number</div>
      <div class="input" style="top:135px;height:62px">Type your Message</div>
      <div class="submit"><div class="ico"><svg width="16" height="12" viewBox="0 0 16 12"><path d="M1 6h12M8 1l5 5-5 5" fill="none" stroke="#dfe07a" stroke-width="1.8"/></svg></div><div class="lbl">SUBMIT</div></div>
    </div>
  </section>

  <section class="about">
    <h2 class="abs section-title" style="left:110px;top:494px">About Us</h2>
    <div class="abs about-text">
      <p>Lorem ipsum dolor sit amet, consectetuer adipiscing elited diam nonummy nibh euismod tincidunt ut laoree tiki dolore magna aliquam erat volutpat. Utminimveilov niam, quis nostrud exerci tation ullamcorper.</p>
      <p>Quam nunc putamus parum claram, anteposuerit litter arum formas humanitatis per seacula quarta decima et quinta decima. Eodem modo typi, qui nunc nobis viden tur parum clari, fiant sollemnes in futurum.</p>
    </div>
    <div class="abs btn-more" style="left:109px;top:704px;width:100px"><b>&gt;</b>Read More</div>
  </section>

  <section class="abs news">
    <div class="news-date" style="top:17px">08-07-2013</div>
    <div class="news-sep" style="top:18px;height:14px"></div>
    <div class="news-sep" style="top:42px;height:103px"></div>
    <div class="news-title" style="left:118px;top:15px">Top Loan Advisor</div>
    <svg class="abs" style="left:603px;top:20px" width="12" height="8" viewBox="0 0 12 8"><path d="M1 1l5 5 5-5" fill="none" stroke="#888" stroke-width="1.4"/></svg>
    <div class="news-photo" role="img" aria-label="Photo of two colleagues talking in an office"></div>
    <div class="news-body">Lorem ipsum dolor sit amet, consectetuer adipiscing elit, sed diam nonummy nibh euismod tincidunt ut laoreet dolore magna aliquam erat volutpat.<br>Ut wisi enim ad minim veniam, quis nostrud exerci tation ullamcorper susconsectet.</div>
    <div class="news-more">&gt; Read More</div>
    <div class="news-row" style="top:166px">
      <div class="news-date date">08-07-2013</div><div class="news-sep" style="top:11px;height:14px"></div>
      <div class="news-title" style="left:122px">Funding for Lending scheme to encourage banks</div>
      <div class="go"><svg width="7" height="11" viewBox="0 0 7 11"><path d="M1 1l4.5 4.5L1 10" fill="none" stroke="#fff" stroke-width="1.4"/></svg></div>
    </div>
    <div class="news-row" style="top:201px">
      <div class="news-date date">08-07-2013</div><div class="news-sep" style="top:11px;height:14px"></div>
      <div class="news-title" style="left:119px">Average loan officer compensation at lenders was $86,300</div>
      <div class="go"><svg width="7" height="11" viewBox="0 0 7 11"><path d="M1 1l4.5 4.5L1 10" fill="none" stroke="#fff" stroke-width="1.4"/></svg></div>
    </div>
  </section>

  <section class="worldwide">
    <div class="abs rule" style="top:787px"></div>
    <div class="abs map" role="img" aria-label="Light grey world map"></div>
    <p class="abs world-text">We are offering non performing loans and our customers are able to invest from 10,000usd to 1,000,000usd (average 50,000usd) and having stong partnership worldwide.</p>
    <div class="abs btn-more" style="left:377px;top:899px;width:100px;height:30px;line-height:30px"><b>&gt;</b>Read More</div>
    <div class="abs feature" style="top:811px"><div class="dot"><svg width="18" height="18" viewBox="0 0 18 18"><circle cx="7" cy="7" r="4.5" fill="none" stroke="#fff" stroke-width="2"/><path d="M10.5 10.5l5 5" stroke="#fff" stroke-width="2.4"/></svg></div><span>Analysis</span></div>
    <div class="abs feature" style="top:855px"><div class="dot"><svg width="16" height="18" viewBox="0 0 16 18"><path d="M4 8V5.5a4 4 0 018 0V8" fill="none" stroke="#fff" stroke-width="2"/><rect x="2" y="8" width="12" height="9" fill="#fff"/><rect x="7" y="11" width="2" height="3" fill="#f7941d"/></svg></div><span>Security</span></div>
    <div class="abs feature" style="top:899px"><div class="dot"><svg width="20" height="20" viewBox="0 0 20 20"><circle cx="10" cy="10" r="8" fill="none" stroke="#fff" stroke-width="1.6"/><path d="M10 4.5V10l-3 3" fill="none" stroke="#fff" stroke-width="1.6"/></svg></div><span>Time</span></div>
  </section>

  <section class="our-clients">
    <h2 class="abs section-title" style="left:109px;top:990px">Our Clients</h2>
    <div class="abs rule" style="top:1021px"></div>
    <div class="abs clients">
      <div class="client"><i></i>Northwire</div>
      <div class="client"><i></i>Thinkfold</div>
      <div class="client"><i></i>Stratum Nine</div>
      <div class="client"><i></i>Rewire Works</div>
      <div class="client"><i></i>Steadfast</div>
    </div>
    <div class="abs rule" style="top:1112px"></div>
  </section>

  <footer class="abs footer">
    <h3 style="left:109px">Quick Links</h3>
    <ul class="quick"><li>Home</li><li>About Us</li><li>Auction</li><li>Access</li><li>Initiation</li><li>Contact Us</li></ul>

    <h3 style="left:307px">Latest Tweets</h3>
    <div class="tweet" style="top:74px"><div class="avatar" role="img" aria-label="Profile photo"></div><div class="name">Mrs. Dana Morell</div><div class="msg">Lorem ipsum dolor sit amet, consectetuer adipiscing elit, sed diam noil<br>nummy nibh euismod tincidunt ut.</div></div>
    <div class="tweet-rule"></div>
    <div class="tweet" style="top:152px"><div class="avatar" role="img" aria-label="Profile photo"></div><div class="name">Mr. Tomas Rivel</div><div class="msg">Lorem ipsum dolor sit amet, consectetuer adipiscing elit, sed diam non<br>ummy nibh euismod tincidunt ut.</div></div>

    <h3 style="left:799px">Contact Us</h3>
    <div class="address">Av Jardines del Valle 412-105,<br>Col. Colinas del Parque, Prov. San Rafael,<br>CP 11500, Mexico DF</div>
    <div class="phone"><svg width="11" height="9" viewBox="0 0 11 9"><path d="M0 3c2-3 9-3 11 0l-2 1.5-1.5-1.5h-4L2 4.5z" fill="#aaa"/><rect x="2" y="5" width="7" height="4" fill="#aaa"/></svg>(55) 4100-3800</div>
    <div class="mail"><svg width="11" height="8" viewBox="0 0 11 8"><rect width="11" height="8" fill="#aaa"/><path d="M0 0l5.5 4.5L11 0" fill="none" stroke="#383838" stroke-width="1"/></svg>ventas@bramley.mx</div>
    <div class="social" style="left:799px"></div>
    <div class="social" style="left:827px"></div>
  </footer>

  <div class="abs bottom-bar">
    <div class="copy">All contents © 2013 Bramley. All rights reserved.</div>
    <div class="links"><span>Site Map</span><span>Term of use</span><span>Privacy Policy</span></div>
  </div>

</div>
</body>
</html>
```